Brightwell Wiring Needs A Logo Design

We need a logo for my new company based out of Sacramento, Ca called Brightwell Wiring. The name says it all, my electrical contracting business provides "Brightwell Craftsman Work" I'm open to any colors that pop and customers to say Wow. I would love to print my cards on metal.

Contact Information for Business Card

The card needs to have as follows
Name of company: Brightwell Wiring
My Name: Marco Delvane
Phone # 916-555-0147
CL# 4873920
Email: brightwellwiring@mailtorva.com
and a slogan that represent "BRIGHTWELL"

Requirements
Must have
• The card needs to have as follows
• Name of company: Brightwell Wiring
• My Name : Marco Delvane
• Phone # 916-555-0147
• CL# 4873920
• Email: brightwellwiring@mailtorva.com
• and a slogan that represent "BRIGHTWELL"
Nice to have
• popping colors
• electrical Arcing

```html
<!DOCTYPE html>
<html lang="en">
<head>
<meta charset="utf-8">
<title>Brightwell Wiring – Business Card</title>
<link rel="stylesheet" href="https://fonts.googleapis.com/css2?family=Arimo:wght@400;700&display=swap">
<style>
  :root {
    --page: #ffffff;
    --navy-core: #1d1f4e;
    --navy-edge: #0f1226;
    --ink-white: #ffffff;
    --accent-yellow: #f7c513;
    --contact-grey: #e9eaf2;
  }
  html, body {
    margin: 0;
    padding: 0;
    width: 1200px;
    height: 999px;
    overflow: hidden;
    background: var(--page);
  }
  .canvas {
    position: relative;
    width: 1200px;
    height: 999px;
    font-family: "Arimo", Arial, sans-serif;
  }
  .card {
    position: absolute;
    left: 79px;
    top: 210px;
    width: 1051px;
    height: 600px;
    overflow: hidden;
    background:
      radial-gradient(ellipse 75% 80% at 35% 40%, var(--navy-core) 0%, #1a1c44 40%, var(--navy-edge) 100%);
  }
  .arc-glow {
    position: absolute;
    inset: 0;
    background:
      radial-gradient(circle 26px at 881px 310px, rgba(255,255,255,1) 0%, rgba(255,255,255,0.9) 55%, rgba(255,255,255,0) 100%),
      radial-gradient(circle 150px at 881px 310px, rgba(150,190,215,0.55) 0%, rgba(90,130,170,0.28) 40%, rgba(60,90,130,0.1) 70%, rgba(60,90,130,0) 100%),
      radial-gradient(ellipse 200px 250px at 930px 470px, rgba(200,215,235,0.16) 0%, rgba(200,215,235,0.06) 60%, rgba(200,215,235,0) 100%);
  }
  .brand {
    position: absolute;
    left: 68px;
    top: 66px;
    width: 457px;
    color: var(--ink-white);
    font-weight: 700;
    line-height: 1;
  }
  .brand-name {
    display: block;
    font-size: 96px;
    letter-spacing: -1px;
  }
  .brand-trade {
    display: block;
    font-size: 52px;
    text-align: right;
    margin-top: 7px;
  }
  .holder-name {
    position: absolute;
    left: 68px;
    top: 363px;
    margin: 0;
    font-size: 45px;
    font-weight: 700;
    color: var(--accent-yellow);
  }
  .contact {
    position: absolute;
    left: 68px;
    top: 446px;
    margin: 0;
    font-size: 26px;
    font-weight: 400;
    line-height: 35px;
    color: var(--contact-grey);
    font-style: normal;
  }
  .contact span { display: block; }
</style>
</head>
<body>
<div class="canvas">
  <section class="card">
    <div class="arc-glow" role="img" aria-label="Glowing electric arc illustration with a bright starburst flare"></div>

    <div class="brand">
      <span class="brand-name">Brightwell</span>
      <span class="brand-trade">WIRING</span>
    </div>

    <h1 class="holder-name">Marco Delvane</h1>

    <address class="contact">
      <span>Phone # 916-555-0147</span>
      <span>CL# 4873920</span>
      <span>Email: brightwellwiring@mailtorva.com</span>
    </address>
  </section>
</div>
</body>
</html>
```